Vemra. Packaging for mood-boosting energy drink mix. Upbeat and uplifting.

I need a mockup of a pouch package + a stick. I included an image of a Aqua Tarn pouch + stick for reference. I do not have a die line for the pouch, so feel free to just use the same relative dimensions for the pouch and create a rendering. Here are the specifications for the packaging that I need:
1. The logo is included in the uploaded files. Please use the one that says "bright day spark" beneath "vemra." The logo should take up about the top 1/3 to 1/2 of the pouch.
2. The pouch should be mostly white, especially behind the logo, but feel free to explore yellow or orange for the bottom 1/2 to 2/3 of the packaging.
3. In the center of the packaging, below the logo, please have the product name appear, "mood-boosting energy drink mix" similar to where "Fluid Amplifier" is placed.
4. Below that, create an image of a glass with a stick pouring into it like in the Aqua Tarn pouch.
5. Below the glass, in the bottom center of the package, include "16 sticks. Net Wt. 4 oz. (114 g)
6. On the left side, please include callouts, from top to bottom, "energy blend (80mg caffeine, taurine) + happy blend (saffron, st. john's wort, rhodiola).
7. On the right side, please include callouts, from top to bottom, "electrolytes + vitamins + 0g sugar"
8. Somewhere else on the front of the packaging, please include the flavor name "golden berry," perhaps where they do on the aqua tarn pouch.
9. For the stick, use your creativity.
10. There is no back of packaging to design for this project.

Target Market(s)

My target consumer leads a very active lifestyle and cares deeply about health & wellness.

Colors
0094D4
00A9DD
6FCCEA
C7EBF8
E9F6FB
FFC000
F8CF3A
FAE287
FDF2CF
FEFAEE
F0912C
F2A743
F7CA91
FBE8D2
FDF5EE
EE7325
F08F49
F5BC92
FAE3D3
FDF4ED

Requirements
Must have
• My packaging must make people feel good and maybe even smile when they see it. A brand that does this well is Penn. (www.pennvita-example.com)
Nice to have
• I like 60's Mod Design if you need some inspiration. The packaging should also convey a sense of levity. Like you'll float or dance through life after drinking this.

```html
<!DOCTYPE html>
<html lang="en">
<head>
<meta charset="utf-8">
<title>Vemra – Pouch and Stick Packaging</title>
<link rel="stylesheet" href="https://fonts.googleapis.com/css2?family=Oswald:wght@400;500&family=Arimo:ital,wght@0,400;0,700;1,700&display=swap">
<style>
  :root {
    --cream: #FEFAEE;
    --orange: #EE7325;
    --orange-mid: #F0912C;
    --orange-soft: #F08F49;
    --orange-deep: #E06A22;
    --yellow: #FFC000;
    --yellow-soft: #F8CF3A;
    --yellow-dark: #DDA817;
    --callout-ink: #8E5511;
    --blue: #0094D4;
    --trim: #E8343A;
    --white: #FFFFFF;
  }
  html, body {
    margin: 0; padding: 0;
    width: 1200px; height: 1199px;
    overflow: hidden;
    background: var(--white);
  }
  .artboard {
    position: relative;
    width: 1250px; height: 1249px;
    transform: scale(0.96);
    transform-origin: 0 0;
    font-family: "Arimo", Arial, sans-serif;
  }
  .abs { position: absolute; }
  .cond { font-family: "Oswald", "Arial Narrow", sans-serif; }

  /* Pouch */
  .pouch {
    left: 112px; top: 168px; width: 730px; height: 949px;
    background: var(--cream);
    outline: 1px solid var(--trim);
    overflow: hidden;
  }
  .pouch-lower {
    left: 0; top: 447px; width: 730px; height: 502px;
    background: radial-gradient(circle at 50% 45%, #F3A04A 0%, var(--orange-mid) 45%, #EE8A3A 100%);
  }
  .pattern-band {
    left: 0; top: 385px; width: 730px; height: 60px;
    background: linear-gradient(90deg, var(--yellow) 0%, var(--orange) 20%, var(--blue) 35%, var(--orange-soft) 50%, var(--yellow) 65%, var(--orange) 80%, var(--yellow) 100%);
  }
  .seam { left: 0; width: 730px; height: 0; border-top: 1px solid var(--trim); }
  .safe {
    left: 49px; top: 0; width: 630px; height: 899px;
    border-left: 1px dashed var(--trim);
    border-right: 1px dashed var(--trim);
    border-bottom: 1px dashed var(--trim);
  }
  .headline { left: 73px; top: 28px; color: var(--orange); }
  .headline .big { font-family: "Oswald", sans-serif; font-size: 30px; line-height: 34px; font-weight: 400; }
  .headline .small { font-size: 18px; font-style: italic; font-weight: 700; color: var(--orange-mid); margin-top: -3px; }
  .count-ribbon { left: 530px; top: 26px; }
  .brand-name {
    left: 0; width: 730px; top: 186px;
    text-align: center; font-weight: 700; font-size: 130px; line-height: 130px;
    color: var(--orange); letter-spacing: -4px;
  }
  .brand-tag { left: 356px; top: 310px; font-weight: 700; font-size: 21px; color: var(--orange); }
  .product-name {
    left: 0; width: 730px; top: 470px; text-align: center;
    color: var(--white); font-size: 43px; line-height: 50px; letter-spacing: -0.5px;
  }
  .callouts { left: 0; top: 560px; }
  .glass-art {
    left: 289px; top: 595px; width: 154px; height: 154px; border-radius: 50%;
    background: linear-gradient(180deg, var(--orange-deep) 0%, var(--orange-deep) 50%, var(--orange) 50%, var(--orange) 100%);
  }
  .flavor-pill {
    background: var(--blue); color: var(--white); border-radius: 18px;
    text-align: center; font-size: 15px;
  }
  .pouch .flavor-pill { left: 289px; top: 794px; width: 144px; height: 36px; line-height: 36px; }
  .net-wt { color: var(--white); font-size: 17px; text-align: center; }
  .pouch .net-wt { left: 0; width: 730px; top: 856px; }

  /* Stick */
  .stick {
    left: 914px; top: 350px; width: 178px; height: 768px;
    background: var(--cream);
    outline: 1px solid var(--trim);
    overflow: hidden;
  }
  .stick-lower {
    left: 0; top: 290px; width: 178px; height: 478px;
    background: linear-gradient(180deg, var(--orange-mid), #EE8A3A);
  }
  .stick-disc {
    left: -3px; top: 290px; width: 184px; height: 178px; border-radius: 50%;
    background: var(--orange-deep);
  }
  .tear-label { left: 11px; top: 26px; font-size: 15px; color: var(--orange); }
  .tear-line { left: 0; top: 53px; width: 178px; border-top: 1px dashed #9A3B20; }
  .stick-brand { left: 0; width: 178px; top: 82px; text-align: center; font-weight: 700; font-size: 56px; line-height: 60px; color: var(--orange); letter-spacing: -2px; }
  .stick-tag { left: 0; width: 178px; top: 168px; text-align: center; font-weight: 700; font-size: 27px; line-height: 31px; color: var(--orange); }
  .stick-product { left: 0; width: 178px; top: 345px; text-align: center; color: var(--white); font-size: 25px; line-height: 27px; }
  .stick-product .line2 { font-size: 21px; }
  .stick-benefits { left: 0; width: 178px; top: 502px; text-align: center; color: var(--yellow); font-size: 22px; line-height: 32px; }
  .stick .flavor-pill { left: 18px; top: 634px; width: 144px; height: 36px; line-height: 36px; }
  .stick .net-wt { left: 0; width: 178px; top: 698px; font-size: 15px; }
  .stick-seal { left: 0; top: 738px; width: 178px; border-top: 1px dashed var(--trim); }
</style>
</head>
<body>
<div class="artboard">

  <section class="pouch abs" aria-label="Pouch front">
    <div class="pouch-lower abs" role="img" aria-label="Warm orange sunburst swirl background"></div>
    <div class="pattern-band abs" role="img" aria-label="Mod half-circle pattern band in yellow, orange and blue"></div>
    <div class="seam abs" style="top:117px"></div>
    <div class="seam abs" style="top:182px"></div>
    <div class="safe abs"></div>

    <div class="headline abs">
      <div class="big">IMPROVE</div>
      <div class="small">your mood easily</div>
    </div>

    <svg class="count-ribbon abs" width="200" height="72" viewBox="0 0 200 72">
      <polygon points="0,0 200,0 200,71 0,71 20,35" fill="var(--blue)"/>
      <text x="43" y="56" fill="#fff" font-family="Oswald, sans-serif" font-size="50">6</text>
      <text x="70" y="31" fill="#fff" font-family="Oswald, sans-serif" font-size="20">STICK</text>
      <text x="70" y="54" fill="#fff" font-family="Oswald, sans-serif" font-size="20">PACKS</text>
    </svg>

    <div class="brand-name abs">vemra</div>
    <div class="brand-tag abs">bright day spark</div>

    <div class="product-name abs cond">MOOD-BOOSTING ENERGY DRINK MIX</div>

    <svg class="callouts abs" width="730" height="380" viewBox="0 560 730 380" font-family="Oswald, sans-serif">
      <!-- left ribbons -->
      <path d="M0,622 H40 V690 H0 Z" fill="var(--yellow-dark)"/>
      <path d="M0,712 H40 V768 H0 Z" fill="var(--yellow-dark)"/>
      <path d="M40,684 C70,684 70,672 110,672" stroke="var(--orange)" stroke-width="8" fill="none"/>
      <path d="M60,572 H228 L253,611 L228,650 H60 Z" fill="var(--yellow-soft)"/>
      <path d="M30,622 H60 V650 H30 Z" fill="var(--yellow-dark)"/>
      <path d="M60,664 H228 L253,714 L228,764 H60 Z" fill="var(--yellow-soft)"/>
      <path d="M30,712 H60 V764 H30 Z" fill="var(--yellow-dark)"/>
      <text x="146" y="604" text-anchor="middle" fill="var(--callout-ink)" font-size="16">ENERGY BLEND</text>
      <text x="146" y="630" text-anchor="middle" fill="var(--callout-ink)" font-size="16">(80mg caffeine, taurine)</text>
      <text x="146" y="697" text-anchor="middle" fill="var(--callout-ink)" font-size="16">HAPPY BLEND</text>
      <text x="146" y="723" text-anchor="middle" fill="var(--callout-ink)" font-size="16">(saffron, st. john's wort,</text>
      <text x="146" y="746" text-anchor="middle" fill="var(--callout-ink)" font-size="16">rhodiola)</text>
      <!-- right ribbons -->
      <path d="M666,630 C690,630 690,670 700,670" stroke="var(--yellow-dark)" stroke-width="22" fill="none"/>
      <path d="M700,642 H730 V670 H700 Z" fill="var(--yellow-soft)"/>
      <path d="M700,683 H730 V710 H700 Z" fill="var(--yellow-soft)"/>
      <path d="M700,722 H730 V752 H700 Z" fill="var(--yellow-soft)"/>
      <path d="M666,700 H700 V736 H666 Z" fill="var(--yellow-dark)"/>
      <path d="M498,572 H666 V629 H498 L473,600 Z" fill="var(--yellow-soft)"/>
      <path d="M498,642 H666 V697 H498 L473,670 Z" fill="var(--yellow-soft)"/>
      <path d="M498,710 H666 V767 H498 L473,738 Z" fill="var(--yellow-soft)"/>
      <text x="578" y="608" text-anchor="middle" fill="var(--callout-ink)" font-size="21">ELECTROLYTES</text>
      <text x="578" y="678" text-anchor="middle" fill="var(--callout-ink)" font-size="21">VITAMINS</text>
      <text x="578" y="747" text-anchor="middle" fill="var(--callout-ink)" font-size="21">0G SUGAR</text>
    </svg>

    <div class="glass-art abs" role="img" aria-label="Glass of water with a stick pack pouring powder into it"></div>

    <div class="flavor-pill abs cond">GOLDEN BERRY</div>
    <div class="net-wt abs">Net Wt. 4 oz. (114 g)</div>
  </section>

  <section class="stick abs" aria-label="Stick pack">
    <div class="stick-lower abs" role="img" aria-label="Warm orange swirl background"></div>
    <div class="stick-disc abs"></div>
    <div class="tear-label abs">Tear Here</div>
    <div class="tear-line abs"></div>
    <div class="stick-brand abs">vemra</div>
    <div class="stick-tag abs">Bright Day<br>Spark</div>
    <div class="stick-product abs cond">MOOD-BOOSTING<br><span class="line2">ENERGY DRINK MIX</span></div>
    <div class="stick-benefits abs cond">ELECTROLYTES<br>VITAMINS<br>0G SUGAR</div>
    <div class="flavor-pill abs cond">GOLDEN BERRY</div>
    <div class="net-wt abs">Net Wt. 4 oz. (114 g)</div>
    <div class="stick-seal abs"></div>
  </section>

</div>
</body>
</html>
```